letter drop flyer

a6 flyer for letterdropping the suburb

I have attached my last one, so something along these lines but my phone number and business card is now different.

```html
<!DOCTYPE html>
<html lang="en">
<head>
<meta charset="utf-8">
<title>Free Market Estimates – Letter Drop Flyer</title>
<link rel="stylesheet" href="https://fonts.googleapis.com/css2?family=Roboto+Condensed:wght@400;700&family=Cabin:wght@600&family=Libre+Baskerville:ital,wght@0,700;1,700&display=swap">
<style>
  :root{
    --brand-blue:#0b5fa8;
    --deep-blue:#0a3f86;
    --sky-top:#9fc3ea;
    --sky-bottom:#eef4fb;
    --orange:#f07a1a;
    --orange-dark:#e2610b;
    --text-grey:#454545;
    --white:#ffffff;
    --paper:#f4f4f4;
  }
  *{margin:0;padding:0;box-sizing:border-box}
  html,body{width:849px;height:1200px;overflow:hidden;background:#fff}
  .flyer{position:relative;width:849px;height:1200px;overflow:hidden;
    background:linear-gradient(180deg,var(--sky-top) 0%,var(--sky-bottom) 40%,#fff 60%,var(--paper) 100%);
    font-family:"Roboto Condensed",Arial,sans-serif}
  .house-photo{position:absolute;left:0;top:150px;width:560px;height:370px;
    background:linear-gradient(180deg,#8b9299 0%,#c9b48f 45%,#a28768 65%,#4f7d36 88%,#3b6a2a 100%)}
  .agent-photo{position:absolute;left:560px;top:0;width:289px;height:420px;
    background:linear-gradient(180deg,#d9e6f3 0%,#c7a98f 30%,#2a2a2e 55%,#1c1c20 100%);
    border-radius:0 0 0 40px}
  .wave{position:absolute;left:0;top:0}
  .brand{position:absolute;left:40px;top:50px;display:flex;align-items:center;gap:9px;white-space:nowrap}
  .brand-square{width:18px;height:18px;background:var(--brand-blue)}
  .brand-name{font-weight:700;font-size:30px;color:var(--brand-blue)}
  .agent-name{position:absolute;left:333px;top:26px;font-weight:700;font-size:37px;line-height:44px;color:var(--brand-blue);white-space:nowrap}
  .agent-mobile{position:absolute;left:333px;top:72px;font-weight:700;font-size:41px;line-height:46px;color:var(--orange);letter-spacing:1px;white-space:nowrap}
  .slogan-badge{position:absolute;left:534px;top:303px;width:290px;height:290px;border-radius:50%;
    border:7px solid var(--white);
    background:radial-gradient(circle at 40% 30%,#2f82d8 0%,var(--brand-blue) 45%,var(--deep-blue) 100%);
    box-shadow:0 4px 12px rgba(0,0,0,.25);
    display:flex;align-items:center;justify-content:center;text-align:center}
  .slogan-badge p{font-family:"Libre Baskerville",Georgia,serif;font-style:italic;font-weight:700;
    color:var(--white);font-size:35px;line-height:1.3;transform:rotate(-10deg)}
  .offer-list{list-style:none}
  .offer{position:absolute;display:flex;align-items:center}
  .offer-letter{flex:none;width:66px;height:66px;border-radius:50%;
    background:radial-gradient(circle at 40% 35%,#ff9a40,var(--orange-dark));
    border:3px solid var(--white);box-shadow:0 1px 4px rgba(0,0,0,.3);
    color:var(--white);font-family:"Libre Baskerville",Georgia,serif;font-weight:700;font-size:34px;
    display:flex;align-items:center;justify-content:center}
  .offer-text{margin-left:28px;font-family:"Cabin",Arial,sans-serif;font-weight:600;
    font-size:26px;line-height:35px;color:var(--text-grey);white-space:nowrap}
  .offer-1{left:61px;top:632px}
  .offer-2{left:185px;top:741px}
  .offer-3{left:61px;top:844px}
  .offer-4{left:185px;top:957px}
  .footer{position:absolute;left:0;top:1060px;width:849px;height:140px;
    border-top:14px solid var(--orange);
    background:linear-gradient(180deg,var(--brand-blue),var(--deep-blue));color:var(--white);font-size:25px}
  .footer-row{position:absolute;display:flex;align-items:center;gap:10px;white-space:nowrap}
  .footer-row svg{fill:var(--white)}
  .sep{margin:0 8px}
  .row-phones{left:36px;top:38px}
  .row-web{left:36px;top:78px}
  .row-address{right:42px;top:38px}
  .row-suburb{right:42px;top:78px}
</style>
</head>
<body>
<div class="flyer">
  <div class="house-photo" role="img" aria-label="Photo of a large two-storey family home with a front lawn"></div>
  <div class="agent-photo" role="img" aria-label="Photo of the agent in a dark business suit presenting with an open hand"></div>

  <svg class="wave" width="849" height="1200" viewBox="0 0 849 1200" aria-hidden="true">
    <defs>
      <linearGradient id="paper" x1="0" y1="0" x2="0" y2="1">
        <stop offset="0" stop-color="#ffffff"/>
        <stop offset="1" stop-color="#ececec"/>
      </linearGradient>
    </defs>
    <path d="M0,485 C220,462 380,420 849,395 L849,470 C400,468 220,510 0,560 Z" fill="var(--orange)"/>
    <path d="M0,560 C220,510 400,468 849,470 L849,1200 L0,1200 Z" fill="url(#paper)"/>
  </svg>

  <div class="brand"><span class="brand-square"></span><span class="brand-name">Northgate Realty</span></div>
  <div class="agent-name">Claire Dunmore</div>
  <div class="agent-mobile">0412 555 318</div>

  <div class="slogan-badge"><p>“You Name it<br>I’ll Sell it”</p></div>

  <ul class="offer-list">
    <li class="offer offer-1"><span class="offer-letter">F</span><span class="offer-text">or this week only I will be providing<br>FREE Market Estimates in your street</span></li>
    <li class="offer offer-2"><span class="offer-letter">R</span><span class="offer-text">ing your local area specialist CLAIRE<br>DUNMORE to arrange a convenient time</span></li>
    <li class="offer offer-3"><span class="offer-letter">E</span><span class="offer-text">stimates are completely FREE with<br>no obligation what so ever</span></li>
    <li class="offer offer-4"><span class="offer-letter">E</span><span class="offer-text">very property will receive a written<br>portfolio of their market estimate</span></li>
  </ul>

  <footer class="footer">
    <div class="footer-row row-phones">
      <svg width="24" height="24" viewBox="0 0 24 24" aria-hidden="true"><path d="M6.6 10.8a15 15 0 006.6 6.6l2.2-2.2c.3-.3.7-.4 1-.2 1.1.4 2.3.6 3.6.6.6 0 1 .4 1 1V20c0 .6-.4 1-1 1A17 17 0 013 4c0-.6.4-1 1-1h3.5c.6 0 1 .4 1 1 0 1.3.2 2.5.6 3.6.1.3 0 .7-.2 1z"/></svg>
      <span>(08) 9555 0142</span><span class="sep">|</span>
      <svg width="26" height="24" viewBox="0 0 26 24" aria-hidden="true"><rect x="6" y="2" width="14" height="6"/><rect x="1" y="9" width="24" height="9" rx="2"/><rect x="6" y="15" width="14" height="7"/></svg>
      <span>(08) 9555 0143</span>
    </div>
    <div class="footer-row row-web"><span>cdunmore@northgate.com.au</span><span class="sep">|</span><span>www.northgate.com.au</span></div>
    <div class="footer-row row-address">
      <svg width="18" height="24" viewBox="0 0 18 24" aria-hidden="true"><path d="M9 0a9 9 0 00-9 9c0 6.8 9 15 9 15s9-8.2 9-15a9 9 0 00-9-9zm0 12.5A3.5 3.5 0 119 5.5a3.5 3.5 0 010 7z"/></svg>
      <span>418b Marlow Street</span>
    </div>
    <div class="footer-row row-suburb"><span>Elmvale WA 6099</span></div>
  </footer>
</div>
</body>
</html>
```